Glow-Mist
Your Source for Stealth Vaping Solutions
I need double sided standard sized Business Card [3.5" x 2"]
I'll leave this up to you, play around w/ some different fonts.Keep it professional. I'm a retailer
Professional
Norris Pellgrave
CEO
Do not list an address on the card.
glowmist.staff@kelvora-mail.net
www.cirro-Q.net
A word about my business: We are a web-based retailer which specializes in electronic cigarettes. I'd like the card to look very professional and clean.
Black should be the dominant color in the scheme, or at least the background. If you can add a subtle pattern into the background that would be nice.
identical background, With a fullsized Cirro-Q logo displayed
Cirro-Q logo
the symbol by itself
this is the variation I want used.

```html
<!DOCTYPE html>
<html lang="en">
<head>
<meta charset="utf-8">
<title>Cirro-Q Business Card</title>
<link rel="stylesheet" href="https://fonts.googleapis.com/css2?family=Josefin+Sans:wght@600&family=Roboto:wght@400;700&display=swap">
<style>
  :root {
    --page-bg: #e9e6e1;
    --card-black: #141414;
    --card-black-edge: #0a0a0a;
    --green-dark: #1e9a2e;
    --green-mid: #3cc23a;
    --green-light: #a7dd3a;
    --yellow-rule: #d6e84a;
    --brand-green: #5bc43a;
    --text-white: #f2f2f2;
    --divider: #5a5a5a;
  }
  html, body {
    margin: 0;
    width: 1200px;
    height: 965px;
    overflow: hidden;
    background: var(--page-bg);
  }
  .business-card {
    position: absolute;
    left: 80px;
    top: 130px;
    width: 1040px;
    height: 705px;
    border-radius: 28px;
    overflow: hidden;
    background:
      repeating-linear-gradient(90deg, rgba(255,255,255,0.015) 0 2px, transparent 2px 6px),
      radial-gradient(ellipse at 50% 40%, #1c1c1c 0%, var(--card-black) 55%, var(--card-black-edge) 100%);
    box-shadow: 0 14px 30px rgba(0,0,0,0.25);
  }
  .edge-band {
    position: absolute;
    top: 0;
    bottom: 0;
    width: 64px;
    background: linear-gradient(180deg, var(--green-dark) 0%, var(--green-mid) 35%, var(--green-light) 60%, var(--green-mid) 80%, var(--green-dark) 100%);
  }
  .edge-band--left { left: 0; border-right: 5px solid var(--yellow-rule); }
  .edge-band--right { right: 0; border-left: 5px solid var(--yellow-rule); }
  .edge-band--left::after, .edge-band--right::after {
    content: "";
    position: absolute;
    top: 0; bottom: 0;
    width: 4px;
    background: #000;
  }
  .edge-band--left::after { right: -9px; }
  .edge-band--right::after { left: -9px; }

  .brand-name {
    position: absolute;
    top: 200px;
    left: 0;
    width: 100%;
    text-align: center;
    font-family: "Josefin Sans", sans-serif;
    font-weight: 600;
    font-size: 96px;
    letter-spacing: 10px;
    color: var(--brand-green);
    margin: 0;
  }
  .holder {
    position: absolute;
    top: 420px;
    right: 595px;
    text-align: right;
    font-family: "Roboto", sans-serif;
  }
  .holder__name {
    margin: 0;
    font-weight: 700;
    font-size: 32px;
    color: var(--brand-green);
  }
  .holder__title {
    margin: 6px 0 0;
    font-size: 25px;
    color: var(--text-white);
  }
  .contact-divider {
    position: absolute;
    left: 478px;
    top: 405px;
    width: 2px;
    height: 180px;
    background: var(--divider);
  }
  .contact-list {
    position: absolute;
    left: 505px;
    top: 405px;
    margin: 0;
    padding: 0;
    list-style: none;
    font-family: "Roboto", sans-serif;
    font-size: 27px;
    color: var(--text-white);
  }
  .contact-list li {
    display: flex;
    align-items: center;
    height: 52px;
  }
  .contact-list svg {
    width: 24px;
    height: 24px;
    margin-right: 16px;
    flex: none;
  }
</style>
</head>
<body>
  <div class="business-card">
    <div class="edge-band edge-band--left"></div>
    <div class="edge-band edge-band--right"></div>

    <h1 class="brand-name">CIRRO-Q</h1>

    <div class="holder">
      <p class="holder__name">Norris Pellgrave</p>
      <p class="holder__title">CEO</p>
    </div>

    <div class="contact-divider"></div>

    <ul class="contact-list">
      <li>
        <svg viewBox="0 0 24 24" aria-hidden="true"><path d="M6.6 2.5c.6-.2 1.2 0 1.5.6l1.8 3.6c.3.5.2 1.1-.2 1.5L8 9.8c1.1 2.4 3.3 4.6 5.7 5.7l1.6-1.7c.4-.4 1-.5 1.5-.2l3.6 1.8c.6.3.8.9.6 1.5l-1 3c-.2.6-.8 1-1.4.9C10.2 20 4 13.8 3.6 5.4c0-.6.3-1.2.9-1.4z" fill="var(--brand-green)"/></svg>
        (555) 014-2276
      </li>
      <li>
        <svg viewBox="0 0 24 24" aria-hidden="true"><circle cx="12" cy="12" r="4" fill="none" stroke="var(--brand-green)" stroke-width="2.4"/><path d="M16 8v5.5c0 1.6 2.8 1.9 3.6-.3A8.5 8.5 0 1 0 15.5 19.8" fill="none" stroke="var(--brand-green)" stroke-width="2.4" stroke-linecap="round"/></svg>
        glowmist.staff@kelvora-mail.net
      </li>
      <li>
        <svg viewBox="0 0 24 24" aria-hidden="true"><g fill="none" stroke="var(--brand-green)" stroke-width="2"><circle cx="12" cy="12" r="9.5"/><ellipse cx="12" cy="12" rx="4.2" ry="9.5"/><path d="M2.5 12h19M4 7h16M4 17h16"/></g></svg>
        www.cirro-Q.net
      </li>
    </ul>
  </div>
</body>
</html>
```